Podcast Artwork

We require a 1440 x 1140px image for a new podcast launching soon. The podcast will be aimed at professionals working in the drug and alcohol treatment sector. The name of the show is The Marlow Ledger.

There is no existing creative for the show for you ti use as reference point.

Target Market(s)

Professionals who work in the drug and alcohol treatment sector.

Industry/Entity Type

Drug

Requirements
Must have
• the stated preferred dimensions given by tessik of Podcast artwork.
Should not have
• Lots of small images of drugs, that's too obvious.

```html
<!DOCTYPE html>
<html lang="en">
<head>
<meta charset="utf-8">
<title>The Marlow Ledger — Podcast Artwork</title>
<link href="https://fonts.googleapis.com/css2?family=Jost:wght@400&display=swap" rel="stylesheet">
<style>
  :root {
    --bg-deep: #2e2e2e;
    --bg-mid: #4a4a4a;
    --bg-light: #5b5b5b;
    --glow: rgba(190, 70, 50, 0.22);
    --title: #ffffff;
  }
  html, body {
    margin: 0;
    padding: 0;
    width: 1200px;
    height: 950px;
    overflow: hidden;
    background: var(--bg-deep);
  }
  .artwork {
    position: relative;
    width: 1200px;
    height: 950px;
    overflow: hidden;
  }
  .neuron-backdrop {
    position: absolute;
    inset: 0;
    background:
      radial-gradient(ellipse at 22% 88%, var(--glow) 0%, transparent 28%),
      radial-gradient(ellipse at 58% 40%, var(--glow) 0%, transparent 22%),
      radial-gradient(ellipse at 45% 45%, var(--bg-light) 0%, var(--bg-mid) 45%, var(--bg-deep) 100%);
  }
  .show-title {
    position: absolute;
    inset: 0;
    margin: 0;
    padding-bottom: 40px;
    display: flex;
    flex-direction: column;
    align-items: center;
    justify-content: center;
    font-family: "Jost", sans-serif;
    font-weight: 400;
    font-size: 246px;
    line-height: 272px;
    letter-spacing: 2px;
    color: var(--title);
    text-transform: uppercase;
  }
  .show-title__line {
    display: block;
  }
</style>
</head>
<body>
  <main class="artwork">
    <div class="neuron-backdrop" role="img" aria-label="Dark grey illustration of a network of neurons with faint red glowing synapses"></div>
    <h1 class="show-title">
      <span class="show-title__line">The</span>
      <span class="show-title__line">Marlow</span>
      <span class="show-title__line">Ledger</span>
    </h1>
  </main>
</body>
</html>
```